Natural Cosmetics need a Packaging Design

We need a PACKAGING design for labels on hand/body wash bottles and soap paper boxes.
We target at high end markets.
We expect a contemporary and trendy design.
We don't need a separate logo. The brand name "Va Mirel" acts as the logo.
We want a modern and classic font for "Va Mirel".
Please see attached pictures for packaging samples.

Industry/Entity Type

Cosmetics

Requirements
Should not have
• a separate logo from the brand name

```html
<!DOCTYPE html>
<html lang="en">
<head>
<meta charset="utf-8">
<title>Va Mirel — Rose and Herbs Packaging</title>
<link rel="stylesheet" href="https://fonts.googleapis.com/css2?family=Federo&family=Cormorant+Garamond:wght@400;500&family=Josefin+Sans:wght@400&display=swap">
<style>
  :root {
    --bg-top: #f6eef1;
    --bg-bottom: #f0dce4;
    --paper: #ffffff;
    --ink: #1d1a1c;
    --plum: #4b1f3b;
    --wash-pink: #e9a3b2;
    --wash-gold: #d9b27a;
    --wash-taupe: #a99a86;
    --wash-lilac: #c6b1c4;
    --title-white: #ffffff;
  }
  * { margin: 0; padding: 0; box-sizing: border-box; }
  html, body { width: 1200px; height: 1200px; overflow: hidden; }
  body {
    background: linear-gradient(180deg, var(--bg-top), var(--bg-bottom));
    position: relative;
    font-family: "Cormorant Garamond", serif;
    color: var(--ink);
  }
  .brand {
    font-family: "Cormorant Garamond", serif;
    font-weight: 500;
    color: var(--ink);
    letter-spacing: 0.02em;
    white-space: nowrap;
  }
  .brand--hero {
    position: absolute;
    top: 92px; left: 0; width: 100%;
    text-align: center;
    font-size: 84px;
  }
  .panel {
    position: absolute;
    top: 280px;
    background: var(--paper);
    overflow: hidden;
    box-shadow: 0 10px 30px rgba(75, 31, 59, 0.12);
  }
  .panel--box { left: 60px; width: 540px; height: 840px; }
  .panel--bottle { left: 640px; width: 500px; height: 840px; }
  .panel .brand--label {
    position: absolute; top: 70px; left: 0; width: 100%;
    text-align: center; font-size: 44px;
  }
  .wash {
    position: absolute; top: 170px; left: 20px; right: 20px; height: 380px;
    border-radius: 48% 52% 44% 56% / 50% 42% 58% 50%;
    background:
      radial-gradient(ellipse at 70% 25%, var(--wash-pink) 0%, transparent 55%),
      radial-gradient(ellipse at 30% 35%, var(--wash-taupe) 0%, transparent 50%),
      radial-gradient(ellipse at 50% 65%, var(--wash-gold) 0%, transparent 55%),
      radial-gradient(ellipse at 15% 80%, var(--wash-lilac) 0%, transparent 50%),
      radial-gradient(ellipse at 85% 75%, var(--wash-pink) 0%, transparent 50%);
    opacity: 0.9;
  }
  .product-name {
    position: absolute; top: 300px; left: 0; width: 100%;
    text-align: center;
    font-family: "Federo", sans-serif;
    color: var(--title-white);
    font-size: 86px;
    line-height: 1;
    text-shadow: 0 2px 6px rgba(60, 30, 20, 0.25);
  }
  .scent {
    position: absolute; top: 590px; left: 0; width: 100%;
    text-align: center;
    font-family: "Cormorant Garamond", serif;
    font-size: 36px;
    letter-spacing: 0.22em;
    color: var(--ink);
  }
  .volume {
    position: absolute; top: 680px; left: 0; width: 100%;
    text-align: center;
    font-family: "Josefin Sans", sans-serif;
    font-size: 26px;
    color: var(--ink);
  }
  .band {
    position: absolute; left: 0; right: 0; bottom: 0; height: 110px;
    background: var(--plum);
    display: flex; align-items: center; justify-content: center;
  }
  .band .brand { color: var(--paper); font-size: 38px; }
</style>
</head>
<body>
  <div class="brand brand--hero">Va Mirel</div>

  <section class="panel panel--box">
    <div class="brand brand--label">Va Mirel</div>
    <div class="wash" role="img" aria-label="Soft watercolour wash in rose, gold, taupe and lilac tones"></div>
    <h1 class="product-name">Body Soap</h1>
    <p class="scent">rose and herbs</p>
    <div class="band"><span class="brand">Va Mirel</span></div>
  </section>

  <section class="panel panel--bottle">
    <div class="brand brand--label">Va Mirel</div>
    <div class="wash" role="img" aria-label="Soft watercolour wash in rose, gold, taupe and lilac tones"></div>
    <h1 class="product-name">Shower Gel</h1>
    <p class="scent">rose and herbs</p>
    <p class="volume">16 FL. OZ (500ML)</p>
    <div class="band"></div>
  </section>
</body>
</html>
```